Seven Quiet Steps to Lift the Final Offer on YOUR House - MERVA Real Estate

I have written an E-Book that is called "Seven Quiet Steps to Lift the Final Offer on Your House." The E-Book will be available as a FREE download from my MERVA Real Estate landing page, and also from a Facebook campaign that will be commencing in early September.

The E-Book content is in the WORD document below - I now need for it to be made to look more professional and suitable for publishing and placed on my landing page for download. Please review and send me some proposals for this e-book to be a bit more eye catching and appealing than just a WORD doc.

My MERVA Real Estate landing page is still under development and you can see the what is close to the final proposal here:

http://www.brell-tovan.com.au/merva/

The cover of the E-Book is at the bottom of the page. Please review and give the internals the sale look and feel.

Target Market(s)

Home and Property Owners in the middle ring Eastern Suburbs of Melbourne - approximately 15 - 30 km's from the central business district. The area is a very family oriented area and features mostly houses that are 3 or 4 bedroom - with some larger properties that are five or more bedrooms. The area is quite an expensive suburban community and house prices range between the low of $1,000,000 to a high of more than $2,500,000. The predominant cultural group that buys in this area are Chinese and Chinese Australian buyers. The predominant group who are selling are usually Australians of a white anglo-saxon background. Other groups are of Asian sub continent background (Indian / Sri Lankan/ Pakistan). All are families that are attracted to the area because of the great schools, good shopping, leisure facilities (parks, pools, courts etc), and excellent public and road transport infrastructure. Read the content of my e-book - it tells you every thing you need to know :)

Industry/Entity Type

Real Estate

Colors

Designer to choose colors to be used in the design.

Requirements
Must have
• Once completed the layout should not be too busy - it should be easy to read. I guess then the statement "less is more" is applicable.
• I will probably print a number of copies of this book for distribution as well - so please consider print attributes in the design.
• IMPORTANT: as for any e-book offering specialist advice, the MAIN reason for the book is for the generation of sales leads and to establish the author as a subject matter expert on the topic. Please consider this in your design elements. BUT - the book should also not come across as 1 big advertisement either. Subtle but impactful are well chosen words to describe how it should present.
Nice to have
• MERVA Real Estate branding on every page - to re-inforce the message.
Should not have
• No need for animations or illustrations/

```html
<!DOCTYPE html>
<html lang="en">
<head>
<meta charset="utf-8">
<title>Seven Quiet Steps to Lift the Final Offer on YOUR House - MERVA Real Estate</title>
<link rel="stylesheet" href="https://fonts.googleapis.com/css2?family=Raleway:wght@300;400;600;700&family=Roboto+Condensed:wght@400;700&display=swap">
<style>
:root{
  --green:#4fbf9a;
  --ink:#231f20;
  --grey:#6d6e71;
  --rule:#c9c9c9;
  --paper:#ffffff;
  --stage:#1d1d1d;
  --head:"Raleway",sans-serif;
  --body:"Roboto Condensed",sans-serif;
}
*{margin:0;padding:0;box-sizing:border-box}
html,body{width:1077px;height:1200px;overflow:hidden;background:var(--stage)}
.spread{position:absolute;left:224px;width:760px;height:537px;transform:scale(.8286);transform-origin:0 0;background:var(--paper);font-family:var(--head);color:var(--ink);overflow:hidden;font-variant-numeric:lining-nums}
.spread--cover{top:81px}
.spread--intro{top:674px}
.shapes{position:absolute;inset:0;width:760px;height:537px}
.abs{position:absolute}

/* brand name */
.brand{font-family:var(--head);font-weight:600;color:var(--ink);line-height:1;letter-spacing:1px;text-align:center}
.brand small{display:block;font-size:.2em;letter-spacing:.55em;margin-top:3px;padding-left:.55em}
.brand--light{color:#fff}

/* cover */
.cover-logo{right:20px;top:250px;font-size:31px}
.cover-number{left:404px;top:285px;font-size:106px;font-weight:700;color:var(--green);line-height:1;font-variant-numeric:lining-nums;font-feature-settings:"lnum" 1}
.cover-title{left:410px;top:384px;text-transform:uppercase;line-height:1.08}
.cover-title span{display:block}
.t-light{font-weight:300;color:var(--grey)}
.t-bold{font-weight:700;color:var(--ink)}
.t-green{font-weight:700;color:var(--green)}
.cover-title .s1{font-size:17px}
.cover-title .s2{font-size:20px}
.cover-title .s3{font-size:25px}
.cover-title .s4{font-size:20px}
.cover-title .s5{font-size:17px}
.rule{height:1px;background:var(--rule)}
.rule::before{content:"";position:absolute;left:0;top:-1px;height:3px;width:36px;background:var(--green)}
.cover-rule{left:410px;top:494px;width:308px}
.cover-area{left:410px;top:505px;font-size:9.5px;letter-spacing:.3px;color:var(--grey);text-transform:uppercase}
.cover-area b{color:var(--ink);font-weight:700}

.contact-lead{left:35px;top:442px;font-family:var(--body);font-size:9px;color:var(--grey);text-transform:uppercase}
.contact-logo{left:35px;top:455px;font-size:25px;text-align:left}
.contact-logo small{padding-left:0}
.contact-rule{left:35px;top:494px;width:307px}
.contact-item{top:505px;font-family:var(--body);font-size:8.5px;color:var(--grey);display:flex;align-items:center;gap:3px}
.contact-item svg{width:8px;height:8px}

/* intro spread */
.portrait-panel{left:26px;top:30px;width:164px;height:464px;background:var(--ink)}
.portrait{position:absolute;left:10px;top:86px;width:144px;height:262px;background:linear-gradient(180deg,#3a3a3a 0%,#1a1a1a 55%,#2b2b2b 100%);border-radius:40px 40px 0 0}
.panel-title{position:absolute;left:12px;top:348px;text-transform:uppercase;line-height:1.08;color:#fff}
.panel-title span{display:block}
.panel-title .light{font-weight:300;font-size:15.5px}
.panel-title .green{font-weight:700;color:var(--green);font-size:20.5px}

.intro-copy{left:208px;top:166px;width:135px;font-family:var(--body);font-size:8.2px;line-height:13.7px;color:var(--grey);text-align:justify}
.intro-copy p+p{margin-top:13px}

.location-head{left:433px;top:68px;text-transform:uppercase;line-height:1.1}
.location-head span{display:block}
.location-head .l1{font-weight:300;font-size:16px;color:var(--ink)}
.location-head .l2{font-weight:700;font-size:18px;color:var(--green)}
.location-head .l3{font-weight:300;font-size:13.5px;color:var(--ink)}

.location-copy{left:433px;top:155px;width:274px;font-family:var(--body);font-size:7px;line-height:10px;color:var(--grey);text-align:justify}
.location-copy ul{list-style:none;margin:8px 0 10px 18px}
.location-copy li{position:relative;margin-bottom:10px}
.location-copy li::before{content:"";position:absolute;left:-10px;top:2px;width:6px;height:6px;background:var(--green)}
.location-copy b{color:var(--ink)}

.footer-rule{top:516px;height:1px;background:var(--rule)}
.footer-rule::before{content:"";position:absolute;left:0;top:-1px;height:3px;width:28px;background:var(--green)}
.page-no{top:522px;font-size:10px;font-weight:700;color:var(--green)}
.footer-logo{right:392px;top:512px;font-size:14px}
.footer-logo small{font-size:.22em;margin-top:1px}
.footer-phone{left:690px;top:521px;font-family:var(--body);font-size:8.5px;color:var(--grey);display:flex;align-items:center;gap:3px}
.footer-phone svg{width:8px;height:8px}
</style>
</head>
<body>

<!-- Cover spread: back cover and front cover -->
<section class="spread spread--cover">
  <svg class="shapes" viewBox="0 0 760 537">
    <defs>
      <linearGradient id="houseTone" x1="0" y1="0" x2="1" y2="1">
        <stop offset="0" stop-color="#e4e4e4"/>
        <stop offset=".45" stop-color="#9a9a9a"/>
        <stop offset="1" stop-color="#5c5c5c"/>
      </linearGradient>
    </defs>
    <g role="img" aria-label="Black and white photo of a two-storey family house among tall trees">
      <polygon points="255,0 760,0 760,135 590,279 475,182" fill="url(#houseTone)"/>
    </g>
    <polygon points="590,279 760,135 760,422" fill="#231f20"/>
    <polygon points="472,180 760,420 760,468" fill="#4fbf9a"/>
    <line x1="255" y1="0" x2="312" y2="48" stroke="#4fbf9a" stroke-width="5"/>
  </svg>

  <div class="abs brand brand--light cover-logo">MERVA<small>REAL ESTATE</small></div>

  <div class="abs cover-number">7</div>
  <h1 class="abs cover-title">
    <span class="s1 t-light">Quiet steps to</span>
    <span class="s2 t-bold">Lift the</span>
    <span class="s3 t-green">Final offer</span>
    <span class="s4 t-light">On your</span>
    <span class="s5 t-light">House</span>
  </h1>
  <div class="abs rule cover-rule"></div>
  <div class="abs cover-area"><b>City of</b> Ashvale &amp; Greythorn</div>

  <div class="abs contact-lead">Get in touch with</div>
  <div class="abs brand contact-logo">MERVA<small>REAL ESTATE</small></div>
  <div class="abs rule contact-rule"></div>
  <div class="abs contact-item" style="left:35px">
    <svg viewBox="0 0 10 10"><circle cx="5" cy="5" r="5" fill="#4fbf9a"/><path d="M3.2 2.6l1 .9-.5.7c.4.7.9 1.2 1.6 1.6l.7-.5.9 1-.8.8C4.6 6.8 3.2 5.4 2.9 3.4z" fill="#fff"/></svg>
    1800 555 017
  </div>
  <div class="abs contact-item" style="left:120px">
    <svg viewBox="0 0 10 10"><circle cx="5" cy="5" r="5" fill="#4fbf9a"/><rect x="2.5" y="3.3" width="5" height="3.4" fill="none" stroke="#fff" stroke-width=".7"/><path d="M2.5 3.3L5 5.2 7.5 3.3" fill="none" stroke="#fff" stroke-width=".7"/></svg>
    info@mervarealestate.com
  </div>
  <div class="abs contact-item" style="left:231px">
    <svg viewBox="0 0 10 10"><circle cx="5" cy="5" r="5" fill="#4fbf9a"/><circle cx="5" cy="5" r="2.6" fill="none" stroke="#fff" stroke-width=".6"/><path d="M2.4 5h5.2M5 2.4c-1.3 1.5-1.3 3.7 0 5.2M5 2.4c1.3 1.5 1.3 3.7 0 5.2" fill="none" stroke="#fff" stroke-width=".5"/></svg>
    www.mervarealestate.com
  </div>
</section>

<!-- Inside spread: pages 01 and 02 -->
<section class="spread spread--intro">
  <div class="abs portrait-panel">
    <div class="portrait" role="img" aria-label="Portrait of the agent in a dark suit and striped tie"></div>
    <div class="panel-title">
      <span class="light">Quiet steps to</span>
      <span class="green">Lift the</span>
      <span class="green">Final offer</span>
      <span class="light">On your</span>
      <span class="light">House</span>
    </div>
  </div>

  <div class="abs intro-copy">
    <p>So after much careful thought you have made the decision to sell your house. For some of you the home may hold many long and happy memories. For others it may have been bought purely as an investment on the path to greater wealth. Sadly for some others a sale may be needed due to a change in life – a new job, money worries, a separation or even the loss of someone close. Whatever the reason behind your move – once the decision is made, the single most important result is to get the best possible price available in the market place.</p>
    <p>In my free e-book – you will find Seven Quiet Steps to Lift the Final Offer on Your House. It holds some useful tips to help you prepare your home to be put on the market for sale. Then once it is ready – what to do to get top dollar for the sale of your home.</p>
  </div>

  <h2 class="abs location-head">
    <span class="l1">By the way....</span>
    <span class="l2">Congratulations</span>
    <span class="l3">On your choice</span>
    <span class="l3">of location:</span>
  </h2>

  <div class="abs location-copy">
    <p>The leafy City of Ashvale and City of Greythorn are very popular residential areas – and it is easy to see why when you consider all they offer the modern family. The standout features of these two fine areas include:</p>
    <ul>
      <li><b>Superb education options:</b> some of the city's leading public and private primary and secondary schools sit within the borders of both councils. There are also strong tertiary options nearby including Ashvale University (north campus), Greythorn Tech (east campus), the Eastern Arts College and the Police Academy, amongst others close to the area. A wide range of childcare and kindergarten choices rounds out a fine list of K-12 options and beyond for local residents.</li>
      <li><b>Outstanding shopping</b> exists at large centres such as Ashvale Plaza, Greythorn Village, Northgate Square and Hillside Central, as well as a number of smaller strip shops and local centres.</li>
      <li><b>Beautiful parks, gardens, trails and outdoor leisure facilities</b> including Lakeside Reserve, Creek Linear Trail, Wattle Sanctuary, Ashvale Golf Club, Greythorn Public Course and many other sporting fields and grounds.</li>
      <li>A large number of <b>public transport choices</b> for commuters and students across the region including trains, trams and buses.</li>
      <li><b>Excellent freeway and road infrastructure</b> that keeps improving and links the area to the wider city. All parts of town are easily reached from both councils.</li>
    </ul>
    <p>Education, shopping, leisure and transport form the backbone of any desirable community – and draw families, investors and builders to these popular and well established areas. The base for interest in your property is already in place. So to help your home sell well at the best price, here are the Seven Quiet Steps to Lift the Final Offer on Your House to help you on your journey.</p>
  </div>

  <div class="abs footer-rule" style="left:0;width:370px"></div>
  <div class="abs page-no" style="left:14px">01</div>
  <div class="abs brand footer-logo">MERVA<small>REAL ESTATE</small></div>

  <div class="abs footer-rule" style="left:380px;width:380px"></div>
  <div class="abs page-no" style="left:393px">02</div>
  <div class="abs footer-phone">
    <svg viewBox="0 0 10 10"><circle cx="5" cy="5" r="5" fill="#4fbf9a"/><path d="M3.2 2.6l1 .9-.5.7c.4.7.9 1.2 1.6 1.6l.7-.5.9 1-.8.8C4.6 6.8 3.2 5.4 2.9 3.4z" fill="#fff"/></svg>
    1800 555 017
  </div>
</section>

</body>
</html>
```